plovu business card design

plovu is an incubator within RTM Media focused on unlocking the potential in underserved niche micro-verticals on the web. our mission is to rapidly develop and foster emerging micro-verticals bc they are ripe for growth - building interesting and trusted content experiences with unqiue, useful and cutting-edge delivery methods.please do all copy (except for RTM Media, which must look as typed here and in logo) in all lowercase. Also please use spaces between phone # extensions not dashes or periods. I have attached all variations of the logo.
Industry/Entity Type
Business
Contact Information for Business Card
daria feltow, ceo www.plovu.io 218 holbrook lane 3rd floor oakland ca 94731 415 602 0002m 510 985 7966d daria.feltow@plovu.io
Look and feel
Each slider illustrates characteristics of the customer's brand and the style your logo design should communicate.

```html
<!DOCTYPE html>
<html lang="en">
<head>
<meta charset="utf-8">
<title>plovu business card</title>
<link rel="stylesheet" href="https://fonts.googleapis.com/css2?family=Quicksand:wght@500;600&family=Source+Sans+3:wght@400&display=swap">
<style>
  :root {
    --backdrop: #d9d2ca;
    --card: #eeebe7;
    --ink: #1e1c1b;
    --teal: #1f6f70;
    --text: #2a2a2a;
    --logo-light: #f1eeea;
    --sub-light: #cfcac4;
  }
  * { margin: 0; padding: 0; box-sizing: border-box; }
  html, body { width: 1200px; height: 1200px; overflow: hidden; }
  body { background: var(--backdrop); position: relative; font-family: "Source Sans 3", sans-serif; }

  .card {
    position: absolute; left: 80px; top: 288px; width: 1040px; height: 624px;
    background: var(--card); border-radius: 6px; overflow: hidden;
    box-shadow: 0 2px 10px rgba(0,0,0,0.08);
  }
  .ink-splash { position: absolute; left: 0; top: 0; width: 560px; height: 624px; }

  .brand { position: absolute; left: 72px; top: 250px; display: flex; align-items: center; gap: 12px; }
  .brand-name {
    font-family: "Quicksand", sans-serif; font-weight: 600; font-size: 96px;
    color: var(--logo-light); line-height: 1; letter-spacing: 1px;
  }
  .brand-dot { width: 22px; height: 22px; border-radius: 50%; background: var(--teal); margin-top: 20px; }
  .brand-tagline {
    position: absolute; left: 72px; top: 382px;
    font-family: "Quicksand", sans-serif; font-weight: 500; font-size: 23px; color: var(--sub-light);
  }

  .person { position: absolute; right: 68px; top: 50px; text-align: right; }
  .person-name { font-family: "Quicksand", sans-serif; font-weight: 600; font-size: 36px; color: var(--teal); line-height: 1.1; }
  .person-title { font-size: 22px; color: var(--text); margin-top: 8px; }

  .contact-list { position: absolute; right: 68px; top: 386px; list-style: none; }
  .contact-item { display: flex; justify-content: flex-end; align-items: center; gap: 18px; height: 34px; font-size: 23px; color: var(--text); }
  .contact-item svg { width: 18px; height: 18px; fill: var(--teal); flex: none; }
  .accent { color: var(--teal); }
  .address { position: absolute; right: 68px; top: 532px; font-size: 25px; color: var(--text); }
</style>
</head>
<body>
  <main class="card">
    <svg class="ink-splash" role="img" aria-label="black ink splash illustration" viewBox="0 0 560 624">
      <path fill="var(--ink)" d="M0 70 C90 40 170 10 250 40 C340 60 420 110 470 190 C520 260 540 330 520 420 C500 510 430 590 330 610 C240 630 120 620 0 610 Z"/>
    </svg>

    <div class="brand">
      <span class="brand-name">plovu</span>
      <span class="brand-dot"></span>
    </div>
    <p class="brand-tagline">an RTM Media incubator</p>

    <div class="person">
      <h1 class="person-name">Daria Feltow</h1>
      <p class="person-title">CEO</p>
    </div>

    <ul class="contact-list">
      <li class="contact-item"><span>94731 415 738 4196m</span>
        <svg viewBox="0 0 24 24"><path d="M3 9c0-3 4-5 9-5s9 2 9 5v2h-5V9H8v2H3z M6 12h12l2 8H4z"/></svg></li>
      <li class="contact-item"><span>510 247 3859d</span>
        <svg viewBox="0 0 24 24"><path d="M7 1h10a2 2 0 0 1 2 2v18a2 2 0 0 1-2 2H7a2 2 0 0 1-2-2V3a2 2 0 0 1 2-2zm0 3v14h10V4z"/></svg></li>
      <li class="contact-item"><span>daria.feltow@plovu.io</span>
        <svg viewBox="0 0 24 24"><path d="M2 5h20v14H2z M3 6l9 7 9-7v1l-9 7-9-7z" fill-rule="evenodd"/></svg></li>
      <li class="contact-item"><span>www.<span class="accent">plovu</span>.io</span>
        <svg viewBox="0 0 24 24"><path d="M12 2a10 10 0 1 0 0 20 10 10 0 0 0 0-20zm-1 2v7H4.1A8 8 0 0 1 11 4zm2 0a8 8 0 0 1 6.9 7H13zM4.1 13H11v7a8 8 0 0 1-6.9-7zM13 13h6.9A8 8 0 0 1 13 20z"/></svg></li>
    </ul>
    <p class="address">218 holbrook lane 3rd floor oakland ca</p>
  </main>
</body>
</html>
```